Online-Marketing Material für Hundetraining
Zielgruppe
Hundetraining. Ich coache Hundehalter und unterstütze sie darin ihrem Hund Führung zu geben. Im Vordergrund steht die natürliche Kommunikation mit dem Hund - komplett ohne Leckerchen.
Aufgabenstellung
Ich brauche ein Design für eine Facebookwerbeanzeige. Der Titel meines Videokurses ist 'Gemeinsam stark im Alltag'. Inhaltlich geht es in dem Kurs darum, wie Hundehalter der akzeptierte Entscheidungsträger werden können, indem wir am Grundrespekt arbeiten und die eigene Führungskompetenzen ausbauen.

```html
<!DOCTYPE html>
<html lang="de">
<head>
<meta charset="utf-8">
<title>Gemeinsam stark im Alltag – Anzeige</title>
<link rel="stylesheet" href="https://fonts.googleapis.com/css2?family=Montserrat:ital,wght@0,400;0,500;0,800;1,700;1,800&family=Open+Sans:wght@700&display=swap">
<style>
  :root {
    --stage: #7b7979;
    --teal: #07b0a8;
    --white: #ffffff;
    --amber: #e09a22;
    --amber-dark: #d48a16;
    --ink: #2b2b2b;
    --fur-light: #f0b97a;
    --fur-mid: #e39a52;
    --fur-deep: #c8702e;
  }
  * { box-sizing: border-box; margin: 0; padding: 0; }
  html, body {
    width: 1200px; height: 864px; overflow: hidden;
    background: var(--stage);
  }
  .ad {
    position: absolute; left: 0; top: 70px;
    width: 1200px; height: 723px;
    background: var(--teal);
    overflow: hidden;
    font-family: "Montserrat", sans-serif;
  }
  .ad__band {
    position: absolute; left: 0; bottom: 0;
    width: 100%; height: 54px;
    background: var(--amber);
  }
  .brand-disc {
    position: absolute; left: 877px; top: -99px;
    width: 320px; height: 320px; border-radius: 50%;
    background: var(--white);
  }
  .brand {
    position: absolute; left: 942px; top: 120px;
    display: flex; align-items: center; gap: 10px;
    z-index: 3;
  }
  .brand__dot {
    width: 22px; height: 22px; border-radius: 50%;
    background: var(--teal);
  }
  .brand__name {
    font-family: "Montserrat", sans-serif;
    font-weight: 800; font-size: 22px;
    color: var(--ink); letter-spacing: 0.3px;
  }
  .photo {
    position: absolute; left: 520px; top: 165px;
    width: 720px; height: 620px;
    border-radius: 48% 40% 0 0 / 42% 38% 0 0;
    background: radial-gradient(ellipse at 45% 40%, var(--fur-light) 0%, var(--fur-mid) 50%, var(--fur-deep) 100%);
    z-index: 2;
  }
  .headline {
    position: absolute; left: 62px; top: 64px;
    transform: rotate(-1.6deg); transform-origin: left top;
    z-index: 4;
  }
  .headline__line {
    display: table;
    background: var(--white);
    color: var(--teal);
    font-size: 74px; line-height: 1;
    text-transform: uppercase;
    padding: 22px 26px 20px 22px;
    margin-bottom: 4px;
    box-shadow: 0 4px 10px rgba(0,0,0,0.12);
  }
  .headline__line:nth-child(2) { margin-left: 4px; }
  .headline__line:nth-child(3) { margin-left: 8px; }
  .headline__bold { font-weight: 800; }
  .headline__light { font-weight: 500; }
  .tagline {
    position: absolute; left: 90px; top: 482px;
    color: var(--white);
    font-weight: 800; font-style: italic;
    font-size: 52px; line-height: 1.25;
    transform: rotate(-2.5deg); transform-origin: left top;
    z-index: 4;
  }
  .cta {
    position: absolute; left: 682px; top: 615px;
    width: 385px; height: 67px; border-radius: 34px;
    background: var(--amber);
    display: flex; overflow: hidden;
    box-shadow: 0 4px 10px rgba(0,0,0,0.2);
    z-index: 5;
  }
  .cta__label {
    flex: 1;
    display: flex; align-items: center; justify-content: center;
    font-family: "Open Sans", sans-serif;
    font-weight: 700; font-size: 29px; letter-spacing: -0.5px;
    color: var(--white);
    padding-left: 12px;
  }
  .cta__icon {
    width: 78px;
    display: flex; align-items: center; justify-content: center;
    background: var(--amber-dark);
  }
</style>
</head>
<body>
  <section class="ad">
    <div class="ad__band"></div>
    <div class="brand-disc"></div>
    <div class="photo" role="img" aria-label="Foto: Zwergspitz mit orangem Fell, dem eine Hand ein Kauleckerli hinhält"></div>
    <div class="brand">
      <span class="brand__dot"></span>
      <span class="brand__name">PFOTENWEG.de</span>
    </div>

    <h1 class="headline">
      <span class="headline__line"><span class="headline__bold">Gemeinsam</span></span>
      <span class="headline__line"><span class="headline__bold">Stark</span> <span class="headline__light">im</span></span>
      <span class="headline__line"><span class="headline__light">Alltag</span></span>
    </h1>

    <p class="tagline">komplett ohne<br>Leckerchen!</p>

    <a class="cta" href="#">
      <span class="cta__label">JETZT ANMELDEN</span>
      <span class="cta__icon">
        <svg width="26" height="28" viewBox="0 0 26 28" aria-hidden="true">
          <path d="M3 2 L24 14 L3 26 Z" fill="#ffffff" stroke="#ffffff" stroke-width="3" stroke-linejoin="round"/>
        </svg>
      </span>
    </a>
  </section>
</body>
</html>
```